Banner Pop Up Opt In Form REDESIGNS - SLEEK BLACK LOOK

Please redesign banners attached.

I am looking for a very sleek look....I do not like this collage of images on these current designs. Please keep all content same but use images that pop.

I have an acccount at www.pixmorrow-example.com or you can use your own images.

I like black background for somereason because it looks very sleek....but these designs should pop , build trust and credibility and have easy opt in form....SLEEK AND MODERN LOOK is what im looking for....

Target Market(s)

Consumers on websites

Requirements
Must have
• Please redesign banners attached.

Nice to have

Should not have

```html
<!DOCTYPE html>
<html lang="en">
<head>
<meta charset="UTF-8">
<title>Smart Fitness Watch – Newsletter Offer</title>
<link rel="stylesheet" href="https://fonts.googleapis.com/css2?family=Montserrat:wght@400;500;700;800&family=Poppins:wght@300;400&display=swap">
<style>
  :root {
    --black: #000000;
    --orange: #f7a11f;
    --white: #ffffff;
    --field: rgba(240, 240, 242, 0.92);
    --field-text: #4a4a4c;
    --photo-dark: #2c2e30;
    --photo-mid: #4d4f52;
    --photo-warm: #5e5354;
  }
  * { margin: 0; padding: 0; box-sizing: border-box; }
  html, body { width: 1200px; height: 1200px; overflow: hidden; background: var(--white); }
  .banner {
    position: relative;
    width: 1200px;
    height: 1200px;
    overflow: hidden;
    font-family: "Montserrat", sans-serif;
  }
  .gym-photo {
    position: absolute;
    inset: 0;
    background:
      radial-gradient(ellipse at 62% 60%, var(--photo-warm) 0%, transparent 55%),
      linear-gradient(160deg, var(--photo-mid) 0%, var(--photo-dark) 100%);
  }
  .hero-shape { position: absolute; inset: 0; width: 1200px; height: 1200px; }
  .headline {
    position: absolute;
    left: 58px;
    top: 44px;
    font-size: 76px;
    font-weight: 800;
    color: var(--orange);
    letter-spacing: 0.5px;
    white-space: nowrap;
  }
  .subline {
    position: absolute;
    left: 61px;
    top: 131px;
    font-size: 26.5px;
    font-weight: 500;
    color: var(--white);
    white-space: nowrap;
  }
  .product-photo {
    position: absolute;
    left: 90px;
    top: 248px;
    width: 233px;
    height: 288px;
    border-radius: 40px;
    background: radial-gradient(ellipse at 50% 45%, #4a4b4d 0%, #262728 55%, #000 100%);
  }
  .product-name { position: absolute; left: 398px; top: 254px; line-height: 1; }
  .product-name .line-one {
    display: block;
    font-size: 60px;
    font-weight: 800;
    color: var(--white);
  }
  .product-name .line-two {
    display: block;
    margin-top: 11px;
    font-size: 96px;
    font-weight: 800;
    color: var(--orange);
  }
  .optin-form { position: absolute; left: 61px; top: 863px; width: 439px; }
  .optin-field {
    display: flex;
    align-items: center;
    height: 54px;
    margin-bottom: 17px;
    padding-left: 41px;
    border-radius: 27px;
    background: var(--field);
    font-family: "Poppins", sans-serif;
    font-size: 27px;
    color: var(--field-text);
  }
  .submit-button {
    position: absolute;
    left: 62px;
    top: 1114px;
    width: 179px;
    height: 48px;
    border-radius: 16px;
    background: var(--orange);
    color: var(--white);
    font-family: "Poppins", sans-serif;
    font-size: 34px;
    line-height: 50px;
    text-align: center;
  }
  .redeem-note {
    position: absolute;
    left: 588px;
    top: 1109px;
    font-family: "Poppins", sans-serif;
    font-weight: 300;
    font-size: 20.5px;
    line-height: 25px;
    color: var(--white);
    white-space: nowrap;
  }
</style>
</head>
<body>
  <div class="banner">
    <div class="gym-photo" role="img" aria-label="Group fitness class doing side plank exercises on a gym floor"></div>

    <svg class="hero-shape" viewBox="0 0 1200 1200" aria-hidden="true">
      <path fill="var(--orange)" d="M0,0 H1054 L1156,200 C1192,268 1180,350 1100,388 L0,752 Z"/>
      <path fill="var(--black)" d="M0,0 H1022 L1126,206 C1154,262 1146,335 1075,363 L0,725 Z"/>
    </svg>

    <h1 class="headline">WANT A GREAT OFFER?</h1>
    <p class="subline">SUBSCRIBE TO OUR NEWSLETTER AND RECIEVE COMPLEMENTARY</p>

    <div class="product-photo" role="img" aria-label="Black fitness tracker watch showing a step count"></div>

    <h2 class="product-name">
      <span class="line-one">SMART FITNESS</span>
      <span class="line-two">WATCH</span>
    </h2>

    <div class="optin-form">
      <div class="optin-field">Name</div>
      <div class="optin-field">Email</div>
      <div class="optin-field">Phone</div>
    </div>
    <div class="submit-button">Submit</div>

    <p class="redeem-note">we will send an email and a text message with the<br>offer and instructions on how to redeem</p>
  </div>
</body>
</html>
```